Title: “The Lantern Path, Rebuilding The Spirit of Harbors, A Sailor’s Journal”

Cover design for ebook and printable book. Looking for this specific designer

```html
<!DOCTYPE html>
<html lang="en">
<head>
<meta charset="utf-8">
<title>The Lantern Path – Book Cover</title>
<link rel="stylesheet" href="https://fonts.googleapis.com/css2?family=Source+Sans+3:wght@400;700;800&display=swap">
<style>
  :root {
    --bg-deep: #060b16;
    --bg-navy: #0b1628;
    --bg-glow: #24465c;
    --text-white: #ffffff;
    --shadow-dark: rgba(0, 0, 0, 0.75);
    --art-red: rgba(226, 62, 58, 0.85);
    --art-pink: rgba(214, 52, 110, 0.6);
    --art-violet: rgba(58, 42, 120, 0.45);
  }
  * { margin: 0; padding: 0; box-sizing: border-box; }
  html, body {
    width: 927px;
    height: 1200px;
    overflow: hidden;
    background: var(--bg-deep);
  }
  .cover {
    position: relative;
    width: 927px;
    height: 1200px;
    overflow: hidden;
    font-family: "Source Sans 3", "Myriad Pro", sans-serif;
    color: var(--text-white);
    background:
      radial-gradient(ellipse 320px 260px at 470px 280px, var(--bg-glow) 0%, rgba(36,70,92,0.35) 55%, rgba(36,70,92,0) 100%),
      linear-gradient(180deg, var(--bg-navy) 0%, #0c1a2c 45%, #0a1322 80%, var(--bg-deep) 100%);
  }
  .cover__floor {
    position: absolute;
    left: 0; right: 0; bottom: 0;
    height: 180px;
    background: radial-gradient(ellipse 420px 40px at 470px 40px, rgba(0,0,0,0.55), rgba(0,0,0,0) 100%);
  }
  .cover__artwork {
    position: absolute;
    left: 151px;
    top: 285px;
    width: 656px;
    height: 720px;
    background: radial-gradient(ellipse 50% 50% at 50% 50%, var(--art-red) 0%, var(--art-pink) 40%, var(--art-violet) 70%, rgba(58,42,120,0) 100%);
  }
  .title-line {
    position: absolute;
    display: block;
    left: 0;
    width: 927px;
    text-align: center;
    line-height: 1;
    white-space: nowrap;
  }
  .title-line--kicker {
    top: 120px;
    left: 17px;
    font-size: 52px;
    font-weight: 400;
  }
  .title-line--lead {
    top: 188px;
    left: 21px;
    font-size: 66px;
    font-weight: 400;
  }
  .title-line--main {
    font-weight: 800;
    letter-spacing: -0.02em;
    text-shadow: 3px 4px 3px var(--shadow-dark);
  }
  .title-line--the   { top: 556px; left: 18px; font-size: 102px; }
  .title-line--noun  { top: 641px; left: 5px;  font-size: 144px; }
  .title-line--of    { top: 769px; left: 18px; font-size: 95px; }
  .title-line--place { top: 846px; left: 22px; font-size: 148px; }
  .title-line--subtitle {
    top: 1003px;
    left: 10px;
    font-size: 47px;
    font-weight: 400;
  }
</style>
</head>
<body>
  <main class="cover">
    <div class="cover__floor"></div>

    <div class="cover__artwork" role="img" aria-label="Cover illustration: a faceted low-poly anatomical heart in red, pink, blue and violet with floating droplets"></div>

    <h1 class="cover__title">
      <span class="title-line title-line--kicker">The Lantern Path,</span>
      <span class="title-line title-line--lead">Rebuilding</span>
      <span class="title-line title-line--main title-line--the">The</span>
      <span class="title-line title-line--main title-line--noun">Spirit</span>
      <span class="title-line title-line--main title-line--of">of</span>
      <span class="title-line title-line--main title-line--place">Harbors,</span>
      <span class="title-line title-line--subtitle">A Sailor’s Journal</span>
    </h1>
  </main>
</body>
</html>
```